COBALT YARDS needs bisness cards pronto

Bisness name is "COBALT YARDS" new bisness the bisness includes lawn mowing, garden matanace, and any jobs around the house.
I need a card that is colorful and vibrant and the bisness of lawn mowing maybe with some nature with it. It also needs my contact details"Desmond Larkwell mobile 0412563049 call for free quote and email gwen.brookvale@fernmail.com and a catchy tag line

Requirements
Must have
• Bisness name "COBALT YARDS"
Contact details "0412563049"
Email gwen.brookvale@fernmail.com
Call for free quote

```html
<!DOCTYPE html>
<html lang="en">
<head>
<meta charset="utf-8">
<title>Cobalt Yards — Business Cards</title>
<link rel="stylesheet" href="https://fonts.googleapis.com/css2?family=Exo+2:wght@300;400&display=swap">
<style>
  :root {
    --bg: #8e8e8e;
    --card: #dac79e;
    --card-deep: #d3be92;
    --ink: #ffffff;
    --stripe: rgba(255, 255, 255, 0.55);
    --stripe-soft: rgba(255, 255, 255, 0.28);
  }
  * { margin: 0; padding: 0; box-sizing: border-box; }
  html, body {
    width: 1200px;
    height: 969px;
    overflow: hidden;
    background: var(--bg);
    font-family: "Exo 2", sans-serif;
    color: var(--ink);
  }
  .card {
    position: absolute;
    left: 300px;
    width: 600px;
    height: 343px;
    background: linear-gradient(160deg, var(--card) 0%, var(--card-deep) 100%);
    box-shadow: 0 6px 18px rgba(0, 0, 0, 0.25);
    overflow: hidden;
  }
  .card--front { top: 100px; }
  .card--back { top: 520px; }
  .card__stripes {
    position: absolute;
    inset: 0;
    width: 600px;
    height: 343px;
  }
  .front__name {
    position: absolute;
    left: 200px;
    top: 118px;
    font-size: 40px;
    font-weight: 300;
    letter-spacing: 1px;
    line-height: 1;
  }
  .back__business {
    position: absolute;
    left: 60px;
    top: 124px;
    font-size: 25px;
    font-weight: 300;
    line-height: 1;
  }
  .back__divider {
    position: absolute;
    left: 262px;
    top: 112px;
    width: 1px;
    height: 96px;
    background: rgba(255, 255, 255, 0.7);
  }
  .contact {
    position: absolute;
    left: 290px;
    top: 112px;
    font-weight: 300;
  }
  .contact__name {
    font-size: 20px;
    line-height: 1;
    margin-bottom: 18px;
  }
  .contact__row {
    display: flex;
    align-items: center;
    gap: 12px;
    font-size: 14px;
    line-height: 1;
    margin-bottom: 12px;
  }
  .contact__row--email { font-size: 11px; letter-spacing: 0.3px; }
  .contact__icon { width: 13px; height: 13px; flex: none; }
  .back__cta {
    position: absolute;
    left: 130px;
    top: 222px;
    font-size: 21px;
    font-weight: 300;
    line-height: 1;
  }
</style>
</head>
<body>

<section class="card card--front" aria-label="Card front">
  <svg class="card__stripes" viewBox="0 0 600 343" aria-hidden="true">
    <polygon points="120,343 190,343 0,95 0,10" fill="var(--stripe)"/>
    <polygon points="205,343 255,343 40,60 0,60 0,88" fill="var(--stripe-soft)"/>
  </svg>
  <div class="front__name">COBALT YARDS</div>
</section>

<section class="card card--back" aria-label="Card back">
  <svg class="card__stripes" viewBox="0 0 600 343" aria-hidden="true">
    <polygon points="115,343 175,343 0,110 0,30" fill="var(--stripe)"/>
    <polygon points="195,343 250,343 45,75 0,75 0,100" fill="var(--stripe-soft)"/>
  </svg>
  <div class="back__business">COBALT YARDS</div>
  <div class="back__divider"></div>
  <div class="contact">
    <div class="contact__name">DESMOND LARKWELL</div>
    <div class="contact__row">
      <svg class="contact__icon" viewBox="0 0 24 24" aria-hidden="true">
        <path fill="#fff" d="M6.6 10.8a15.1 15.1 0 0 0 6.6 6.6l2.2-2.2a1 1 0 0 1 1-.25 11.4 11.4 0 0 0 3.6.57 1 1 0 0 1 1 1V20a1 1 0 0 1-1 1A17 17 0 0 1 3 4a1 1 0 0 1 1-1h3.5a1 1 0 0 1 1 1c0 1.25.2 2.45.57 3.57a1 1 0 0 1-.25 1z"/>
      </svg>
      <span>0412563049</span>
    </div>
    <div class="contact__row contact__row--email">
      <svg class="contact__icon" viewBox="0 0 24 24" aria-hidden="true">
        <path fill="#fff" d="M2 5h20v14H2z"/>
        <path fill="none" stroke="var(--card-deep)" stroke-width="1.6" d="M2.5 5.5 12 13l9.5-7.5"/>
      </svg>
      <span>GWEN.BROOKVALE@FERNMAIL.COM</span>
    </div>
  </div>
  <div class="back__cta">CALL FOR FREE QUOTE</div>
</section>

</body>
</html>
```